PICTURE CALENDAR - CONSTRUCTION COMPANY

- PICTURES CALENDAR 2018 (wall calendar) - graphic design - square 50 x 50 cm - 14 pages (title - months index pages) - languages ​​- german - Italian - construction industry - minimalistic and clear - modern - for each month inkluding logo color www.peltronbau.it

Reason: Sehr geehrte Damen und Herren, bitte um eine Fristverlängerung. Es ist Wochenende und ich selbst bekomme auf kein Feedback ob ein Design jetzt passt oder nicht. Weiters haben wir bereits einen Favoriten welcher aber noch Details abändern müsste. Vielen Dank! Mit freundlichen Grüßen, Matthias Grübel

Target Market(s)

construction worker

Industry/Entity Type

Construction

Font styles to use
Sans Serif

Colors
0355a3
dddddd

Requirements
Must have
• 49 x 49 cm 12 months german italiano short image description including logo
Nice to have
• cool line
Should not have
• the graphic design not playful, no gradients

```html
<!DOCTYPE html>
<html lang="de">
<head>
<meta charset="utf-8">
<title>Kalender Juli / August – peltron bau</title>
<link href="https://fonts.googleapis.com/css2?family=Source+Sans+3:wght@400;600;700;900&display=swap" rel="stylesheet">
<style>
  :root {
    --brand-blue: #0355a3;
    --panel-blue: rgba(3, 85, 163, 0.82);
    --stripe-blue: rgba(40, 90, 170, 0.75);
    --brand-navy: #2b3590;
    --white: #ffffff;
    --light-grey: #dddddd;
  }
  * { margin: 0; padding: 0; box-sizing: border-box; }
  html, body { width: 1200px; height: 1200px; overflow: hidden; }
  body { font-family: "Source Sans 3", sans-serif; color: var(--white); }

  .page { position: relative; width: 1200px; height: 1200px; overflow: hidden; }

  .photo {
    position: absolute; inset: 0;
    background: linear-gradient(180deg,
      #cfdcea 0%, #b9cde3 14%, #c7c2b6 22%, #a9a296 30%,
      #3f5a2f 36%, #4a6130 42%, #8c8a78 45%, #5fa6a8 52%,
      #54a2a4 66%, #9a8a6c 80%, #a08c5e 100%);
  }

  .stripe { position: absolute; left: 94px; width: 279px; background: var(--stripe-blue); }
  .stripe-1 { top: 7px;  height: 3px; }
  .stripe-2 { top: 18px; height: 5px; }
  .stripe-3 { top: 33px; height: 10px; }
  .stripe-4 { top: 53px; height: 21px; }
  .stripe-5 { top: 1127px; height: 21px; }
  .stripe-6 { top: 1157px; height: 10px; }
  .stripe-7 { top: 1177px; height: 5px; }
  .stripe-8 { top: 1193px; height: 3px; }

  .calendar-panel {
    position: absolute; left: 94px; top: 83px; width: 279px; height: 1034px;
    background: var(--panel-blue);
  }

  .month { position: absolute; left: 0; width: 279px; }
  .month-july { top: 93px; }
  .month-august { top: 652px; }

  .month-title {
    text-align: center; font-size: 22px; font-weight: 600; line-height: 1;
  }

  .weekdays, .days {
    position: absolute; left: 6px; width: 266px;
    display: grid; grid-template-columns: repeat(7, 38px);
    text-align: center; font-weight: 600; font-size: 14.5px;
  }
  .weekdays { top: 70px; line-height: 18px; }
  .weekdays span { display: block; }
  .rule {
    position: absolute; left: 14px; width: 250px; top: 120px;
    height: 1px; background: var(--light-grey);
  }
  .days { top: 128px; grid-auto-rows: 38px; line-height: 38px; }

  .brand-band {
    position: absolute; left: 94px; top: 561px; width: 279px; height: 77px;
    background: var(--white); display: flex; align-items: center;
  }
  .brand-mark { width: 77px; height: 77px; background: var(--brand-navy); flex: none; }
  .brand-name {
    position: relative; flex: 1; text-align: center;
    color: var(--brand-navy); font-weight: 900; font-size: 33px;
    letter-spacing: -0.5px; line-height: 1; padding-bottom: 6px;
  }
  .brand-legal {
    position: absolute; right: 18px; bottom: -6px;
    font-size: 5px; font-weight: 600; color: var(--brand-navy); letter-spacing: 0;
  }
</style>
</head>
<body>
<div class="page">
  <div class="photo" role="img" aria-label="Foto: Bagger belädt einen Muldenkipper am Ufer eines Speicherteichs, dahinter Nadelwald und Dolomitengipfel unter blauem Himmel"></div>

  <div class="stripe stripe-1"></div>
  <div class="stripe stripe-2"></div>
  <div class="stripe stripe-3"></div>
  <div class="stripe stripe-4"></div>

  <div class="calendar-panel">
    <section class="month month-july">
      <h2 class="month-title">Juli / Luglio</h2>
      <div class="weekdays">
        <div><span>Mo</span><span>Lu</span></div>
        <div><span>Di</span><span>Ma</span></div>
        <div><span>Mi</span><span>Me</span></div>
        <div><span>Do</span><span>Gi</span></div>
        <div><span>Fr</span><span>Ve</span></div>
        <div><span>Sa</span><span>Sa</span></div>
        <div><span>So</span><span>Do</span></div>
      </div>
      <div class="rule"></div>
      <div class="days">
        <span></span><span></span><span></span><span></span><span></span><span></span><span>1</span>
        <span>2</span><span>3</span><span>4</span><span>5</span><span>6</span><span>7</span><span>8</span>
        <span>9</span><span>10</span><span>11</span><span>12</span><span>13</span><span>14</span><span>15</span>
        <span>16</span><span>17</span><span>18</span><span>19</span><span>20</span><span>21</span><span>22</span>
        <span>23</span><span>24</span><span>25</span><span>26</span><span>27</span><span>28</span><span>29</span>
        <span>30</span><span>31</span>
      </div>
    </section>

    <section class="month month-august">
      <h2 class="month-title">August / Agosto</h2>
      <div class="weekdays">
        <div><span>Mo</span><span>Lu</span></div>
        <div><span>Di</span><span>Ma</span></div>
        <div><span>Mi</span><span>Me</span></div>
        <div><span>Do</span><span>Gi</span></div>
        <div><span>Fr</span><span>Ve</span></div>
        <div><span>Sa</span><span>Sa</span></div>
        <div><span>So</span><span>Do</span></div>
      </div>
      <div class="rule"></div>
      <div class="days">
        <span></span><span></span><span>1</span><span>2</span><span>3</span><span>4</span><span>5</span>
        <span>6</span><span>7</span><span>8</span><span>9</span><span>10</span><span>11</span><span>12</span>
        <span>13</span><span>14</span><span>15</span><span>16</span><span>17</span><span>18</span><span>19</span>
        <span>20</span><span>21</span><span>22</span><span>23</span><span>24</span><span>25</span><span>26</span>
        <span>27</span><span>28</span><span>29</span><span>30</span><span>31</span>
      </div>
    </section>
  </div>

  <div class="brand-band">
    <div class="brand-mark"></div>
    <div class="brand-name">peltron bau<span class="brand-legal">&amp; Co. KG/SAS d. Grübel Matthias</span></div>
  </div>

  <div class="stripe stripe-5"></div>
  <div class="stripe stripe-6"></div>
  <div class="stripe stripe-7"></div>
  <div class="stripe stripe-8"></div>
</div>
</body>
</html>
```